Web-Redesign für Anbieter von immersiver Medienproduktion, Virtual Reality und 360-Grad-Aufnahmen
Zielgruppe
Bei dem Auftrag geht es um ein ReDesign der bestehende Website www.lumorix7.de
Lumorix 7 ist ein Powerhouse für immersive Medienproduktion, Virtual Reality und 360 Grad Aufnahmen. Wir erschaffen faszinierende und verblüffende Customer Experiences über alle Kanäle hinweg. Unsere Markeninszenierungen sind immer am Rande des technisch machbaren und hinterlassen nachhaltigen Eindruck beim Kunden. Dabei ist die Verbindung von hochwertigem Design, cutting-edge Technology und Emotion der Kern unserer Arbeit. Wir sind digital und real. Und Experten darin, Marken neuartig erfahrbar und damit erfolgreich zu machen. Nationale und internationale Kunden aus den Bereichen Automotive, Pharma, TV und Industrie vertrauen uns seit vielen Jahren.
Aufgabenstellung
Wir möchten unseren Slogan 'WE DO THE NEW' in den Fokus stellen und den Fokus auf uns Showreell samt 'Über uns'-Text legen. Wir wollen innovativ, futuristisch und aber klar strukturiert sein. Unser Ziel ist es, ein Termin mit dem potentiellen Interessenten zu haben.

```html
<!DOCTYPE html>
<html lang="de">
<head>
<meta charset="utf-8">
<title>Lumorix 7 – We do the new.</title>
<link href="https://fonts.googleapis.com/css2?family=Montserrat:wght@400;500;600;700;800;900&display=swap" rel="stylesheet">
<style>
:root{
  --navy:#0d2150;
  --navy-soft:#1d3466;
  --cyan:#45e9f0;
  --cyan-deep:#27d6e0;
  --cyan-light:#dff9fc;
  --ice:#effcfd;
  --white:#ffffff;
  --text:#2c3a55;
  --muted:#8a9ab0;
}
*{margin:0;padding:0;box-sizing:border-box}
html,body{width:1200px;height:4265px;overflow:hidden}
body{position:relative;background:var(--white);font-family:'Montserrat',sans-serif;color:var(--text)}
.abs{position:absolute}
.backdrop{position:absolute;left:0;top:0;width:1200px;height:4265px}

/* top bar + nav */
.topbar{left:0;top:0;width:1200px;height:30px;background:var(--navy);color:#fff;font-size:9px;padding:0 160px;display:flex;align-items:center;justify-content:space-between}
.topbar .social{display:flex;gap:8px}
.dot-icon{width:16px;height:16px;border:1.5px solid #fff;border-radius:50%}
.nav{left:0;top:30px;width:1200px;height:91px;background:#fff;display:flex;align-items:center;padding:0 160px;justify-content:space-between}
.brand{font-weight:800;font-size:22px;color:var(--navy);letter-spacing:1px}
.menu{display:flex;gap:34px;align-items:center;font-size:11px;font-weight:700;color:var(--navy)}
.menu .active{color:var(--navy);position:relative}
.menu .active::after{content:"";position:absolute;left:0;right:0;bottom:-8px;height:2px;background:var(--cyan)}
.flag{width:18px;height:12px;background:var(--navy);position:relative;overflow:hidden}
.flag::before{content:"";position:absolute;left:7px;top:0;width:4px;height:12px;background:#e33}
.flag::after{content:"";position:absolute;left:0;top:4px;width:18px;height:4px;background:#e33}

/* hero */
.hero{left:0;top:121px;width:1200px;height:627px;background:radial-gradient(ellipse at 50% 35%,#3a5a8a 0%,#14224a 45%,#050a1c 100%)}
.hero-title{left:0;top:300px;width:1200px;text-align:center;color:#fff;font-weight:900;font-size:86px;line-height:104px;letter-spacing:-1px}
.btn-reel{left:525px;top:551px;width:134px;height:32px;border-radius:16px;background:var(--cyan);color:var(--navy);font-size:11px;font-weight:600;display:flex;align-items:center;justify-content:center;gap:8px;letter-spacing:.5px}
.play{width:14px;height:14px;border:1.5px solid var(--navy);border-radius:50%;position:relative}
.play::after{content:"";position:absolute;left:4px;top:3px;border-left:5px solid var(--navy);border-top:3px solid transparent;border-bottom:3px solid transparent}

/* about */
.eyebrow{font-size:13px;font-weight:500;letter-spacing:1px;color:var(--navy)}
.rule{height:2px;background:var(--cyan)}
.about-title{left:160px;top:900px;font-size:28px;font-weight:700;line-height:33px;color:var(--navy)}
.about-text{left:160px;top:993px;width:378px;font-size:11.6px;line-height:18px;color:var(--text);text-align:justify}
.btn-outline{left:172px;top:1253px;width:166px;height:31px;border:1.5px solid var(--cyan);border-radius:16px;color:var(--cyan);font-size:11px;display:flex;align-items:center;justify-content:center}
.photo{border-radius:12px;box-shadow:0 10px 24px rgba(13,33,80,.25)}

/* services */
.svc-title{font-size:36px;font-weight:800;color:#fff}
.num{font-size:96px;font-weight:900;line-height:1;letter-spacing:-2px}
.svc-head{font-size:22px;font-weight:700;line-height:27px}
.svc-text{font-size:11.6px;line-height:20px;text-align:justify}
.arrow{width:34px;height:10px}

/* clients */
.clients-title{left:160px;top:2988px;font-size:36px;font-weight:800;color:var(--muted)}
.client{font-size:17px;font-weight:700;color:var(--muted);text-align:center;width:130px}

/* contact */
.card{left:160px;top:3219px;width:879px;height:563px;background:#fff;border-radius:8px;box-shadow:0 14px 40px rgba(13,33,80,.15)}
.card h2{position:absolute;left:0;top:52px;width:879px;text-align:center;font-size:23px;font-weight:700;color:var(--cyan)}
.card p{position:absolute;left:160px;top:92px;width:559px;text-align:center;font-size:10px;line-height:18px;color:var(--muted)}
.field{position:absolute;border:1px solid #d5dbe3;border-radius:2px;font-size:9px;font-style:italic;color:var(--muted);padding:10px 12px}
.btn-send{left:528px;top:3699px;width:142px;height:36px;border-radius:18px;background:var(--cyan);color:#fff;font-size:10px;font-weight:700;display:flex;align-items:center;justify-content:center}

/* footer */
.foot-line{left:160px;top:3886px;width:879px;height:1px;background:rgba(255,255,255,.2)}
.foot-brand{left:160px;top:3938px;font-size:24px;font-weight:800;color:#fff;letter-spacing:1px}
.foot-text{color:#fff;font-size:12px;line-height:19px}
.foot-head{color:var(--cyan);font-size:13px;font-weight:700;letter-spacing:1px}
.foot-list{color:#fff;font-size:12px;line-height:29.5px;list-style:none}
.foot-list li::before{content:"> ";color:var(--cyan)}
.copyright{left:0;top:4224px;width:1200px;text-align:center;font-size:10px;color:var(--navy)}
.to-top{left:1027px;top:4188px;width:32px;height:32px;border-radius:50%;background:#e8f0f5;box-shadow:0 4px 10px rgba(0,0,0,.2)}
</style>
</head>
<body>

<svg class="backdrop" viewBox="0 0 1200 4265" aria-hidden="true">
  <polygon points="0,1333 1200,1270 1200,1556 728,1374" fill="#dff9fc"/>
  <polygon points="0,1333 728,1374 1200,1556 1200,1990 0,1990" fill="#45e9f0"/>
  <rect x="0" y="1986" width="1200" height="364" fill="#0d2150"/>
  <polygon points="0,2350 1200,2350 1200,2980 0,2877" fill="#45e9f0"/>
  <polygon points="0,2877 1200,2980 1200,3500 0,3650" fill="#effcfd"/>
  <polygon points="0,3650 1200,3500 1200,4204 0,4204" fill="#0d2150"/>
  <rect x="0" y="4204" width="1200" height="61" fill="#45e9f0"/>
</svg>

<header>
  <div class="abs topbar">
    <span>Lichtbogenweg 7, 82041 Oberhaching</span>
    <span class="social"><span class="dot-icon"></span><span class="dot-icon"></span><span class="dot-icon"></span></span>
  </div>
  <nav class="abs nav">
    <div class="brand">LUMORIX 7</div>
    <div class="menu">
      <span class="active">HOME</span><span>ÜBER UNS</span><span>SERVICES</span><span>KONTAKT</span><span>TERMIN</span><span class="flag"></span>
    </div>
  </nav>
</header>

<section>
  <div class="abs hero" role="img" aria-label="Showreel-Standbild: futuristische Fahrzeugpräsentation auf großen Bildschirmen in blauem Licht"></div>
  <h1 class="abs hero-title">WE DO<br>THE NEW.</h1>
  <div class="abs btn-reel"><span class="play"></span>SHOWREEL</div>
</section>

<section>
  <div class="abs eyebrow" style="left:160px;top:832px">ÜBER UNS</div>
  <div class="abs rule" style="left:160px;top:871px;width:50px"></div>
  <h2 class="abs about-title">Kommen Sie zu uns,<br>wir können Zukunft.</h2>
  <p class="abs about-text">Lumorix 7 ist ein Powerhouse für immersive Medienproduktion, Virtual Reality und 360 Grad Aufnahmen. Wir erschaffen faszinierende und verblüffende Customer Experiences über alle Kanäle hinweg. Unsere Markeninszenierungen sind immer am Rande des technisch machbaren und hinterlassen nachhaltigen Eindruck beim Kunden. Dabei ist die Verbindung von hochwertigem Design, cutting-edge Technology und Emotion der Kern unserer Arbeit. Wir sind digital und real. Und Experten darin, Marken neuartig erfahrbar und damit erfolgreich zu machen. Nationale und internationale Kunden aus den Bereichen Automotive, Pharma, TV und Industrie vertrauen uns seit vielen Jahren.</p>
  <div class="abs btn-outline">Get in Touch &nbsp;→</div>
  <div class="abs photo" style="left:611px;top:965px;width:200px;height:237px;background:linear-gradient(160deg,#6a2a8c,#c0306a 55%,#2a0c3a)" role="img" aria-label="Lichtinstallation mit leuchtenden Punkten vor einem Gebäude bei Nacht"></div>
  <div class="abs photo" style="left:839px;top:829px;width:200px;height:237px;background:linear-gradient(160deg,#1a2a7a,#3a3ac0 50%,#120a4a)" role="img" aria-label="Digitale Hologramm-Projektion mit Zeitanzeige"></div>
  <div class="abs photo" style="left:839px;top:1099px;width:200px;height:237px;background:linear-gradient(160deg,#b04ad8,#5a2a9a 55%,#1a2240)" role="img" aria-label="Person im Motion-Capture-Anzug im Studio"></div>
</section>

<section>
  <div class="abs eyebrow" style="left:162px;top:1429px">WHAT WE DO</div>
  <h2 class="abs svc-title" style="left:160px;top:1451px">Our Services</h2>
  <div class="abs" style="left:444px;top:1476px;width:91px;height:2px;background:#fff"></div>

  <div class="abs photo" style="left:160px;top:1556px;width:375px;height:354px;background:linear-gradient(170deg,#b06ad8,#7a3a9a 45%,#d04a6a 80%,#3a1a4a)" role="img" aria-label="Inszenierung auf rotem Teppich mit Palmen und Publikum"></div>
  <div class="abs num" style="left:610px;top:1578px;color:var(--cyan-deep)">01</div>
  <div class="abs svc-head" style="left:761px;top:1610px;color:var(--navy)">DESIGN &amp;<br>CONTENT CREATION</div>
  <p class="abs svc-text" style="left:612px;top:1693px;width:427px;color:var(--navy)">Wir entwickeln starke Marken und füllen sie mit Leben, um Ihre Marken und Produkte unwiderstehlich zu machen. Wir glauben an klares, einprägsames und hochwertiges Design, das die Kraft emotionaler Geschichten nutzt. Dabei beobachten wir das Markenumfeld und suchen immer nach neuen Wegen, um Ihre Zielgruppe zu erreichen – über Kopf UND Herz. Unsere Expertise umfasst Design für TV-Sender und TV-Formate, TV-Kampagnen, Messebespielungen, Imagefilme, Werbespots und Social Media Filme.</p>
  <svg class="abs arrow" style="left:612px;top:1878px" viewBox="0 0 34 10"><path d="M0 5H32M28 1L32 5L28 9" stroke="#fff" stroke-width="1" fill="none"/></svg>

  <div class="abs num" style="left:158px;top:2060px;color:var(--navy-soft)">02</div>
  <div class="abs svc-head" style="left:339px;top:2086px;color:var(--cyan)">REALTIME<br>EXPERIENCES</div>
  <p class="abs svc-text" style="left:160px;top:2170px;width:428px;color:#fff">Performance TV-Marketing rückt Artikel, die der Zuschauer entdeckt hat, in unmittelbare Interaktionsnähe des Kunden. Denn fast jeder zweite Zuschauer sucht online nach Produkten, die er kurz zuvor im Fernsehen gesehen hat. Richtig abgeholt, wird aus der Recherche ein Verkaufserfolg. Genau darauf sind wir spezialisiert.</p>
  <svg class="abs arrow" style="left:160px;top:2299px" viewBox="0 0 34 10"><path d="M0 5H32M28 1L32 5L28 9" stroke="#fff" stroke-width="1" fill="none"/></svg>
  <div class="abs photo" style="left:665px;top:2060px;width:374px;height:356px;background:linear-gradient(120deg,#e0307a,#c060d0 45%,#e88a50 80%,#f0b070)" role="img" aria-label="Zwei Zuschauer blicken gebannt auf eine Präsentation in buntem Licht"></div>

  <div class="abs photo" style="left:160px;top:2448px;width:376px;height:355px;background:linear-gradient(170deg,#2ab0d8,#1a3a8a 45%,#5a2aa8 75%,#0a1030)" role="img" aria-label="Futuristischer Showroom mit Lichtring und Fahrzeug"></div>
  <div class="abs num" style="left:609px;top:2500px;color:var(--cyan-deep)">03</div>
  <div class="abs svc-head" style="left:773px;top:2533px;color:var(--navy)">REALTIME<br>EXPERIENCES</div>
  <p class="abs svc-text" style="left:611px;top:2616px;width:428px;color:var(--navy)">Sie planen eine Veranstaltung, Messe oder ein besonders Corporate Event auszurichten? Ein Event, welches eine beeindruckende, immersive Erfahrung bietet? Dann lassen Sie uns sprechen. Seit über 20 Jahren arbeiten wir in der professionellen Event-Planung im Bereich Immersive Events. Wir kreieren Ereignisse, die den Zuschauer faszinieren und ihn mittels neuester Technologien in eine andere Welt abtauchen lassen.</p>
  <svg class="abs arrow" style="left:611px;top:2764px" viewBox="0 0 34 10"><path d="M0 5H32M28 1L32 5L28 9" stroke="#fff" stroke-width="1" fill="none"/></svg>
</section>

<section>
  <h2 class="abs clients-title">Kunden</h2>
  <div class="abs rule" style="left:348px;top:3013px;width:190px"></div>
  <span class="abs" style="left:140px;top:3096px;color:var(--muted);font-size:14px">‹</span>
  <span class="abs" style="left:1057px;top:3096px;color:var(--muted);font-size:14px">›</span>
  <div class="abs client" style="left:160px;top:3094px">Nordwelle Media</div>
  <div class="abs client" style="left:309px;top:3094px">Kanal Süd</div>
  <div class="abs client" style="left:458px;top:3094px">Lichtspielwerk</div>
  <div class="abs client" style="left:607px;top:3094px">reisefix</div>
  <div class="abs client" style="left:756px;top:3094px">Bergblick TV</div>
  <div class="abs client" style="left:905px;top:3094px">arena5</div>
  <span class="abs" style="left:575px;top:3155px;width:8px;height:8px;border-radius:50%;border:1.5px solid var(--muted)"></span>
  <span class="abs" style="left:597px;top:3155px;width:8px;height:8px;border-radius:50%;background:#cfdbe4"></span>
  <span class="abs" style="left:620px;top:3155px;width:8px;height:8px;border-radius:50%;background:#cfdbe4"></span>
</section>

<section>
  <div class="abs card">
    <h2>GET IN TOUCH!</h2>
    <p>Lorem ipsum dolor sit amet consectetur adipiscing elit donec tempus pellentesque dui vel tristique purus justo vestibulum eget lectus non gravida ultrices</p>
    <div class="field" style="left:53px;top:164px;width:378px;height:35px">Your Name *</div>
    <div class="field" style="left:454px;top:164px;width:377px;height:35px">Phone Number *</div>
    <div class="field" style="left:53px;top:222px;width:378px;height:36px">Email *</div>
    <div class="field" style="left:454px;top:222px;width:377px;height:36px">Subject</div>
    <div class="field" style="left:53px;top:281px;width:778px;height:163px">Message</div>
  </div>
  <div class="abs btn-send">SEND US MESSAGE</div>
</section>

<footer>
  <div class="abs foot-line"></div>
  <div class="abs foot-brand">LUMORIX 7</div>
  <svg class="abs" style="left:160px;top:4004px" width="14" height="18" viewBox="0 0 14 18"><path d="M7 17C7 17 1 10 1 6.5A6 6 0 0 1 13 6.5C13 10 7 17 7 17Z" stroke="#45e9f0" fill="none" stroke-width="1.4"/><circle cx="7" cy="6.5" r="2" stroke="#45e9f0" fill="none"/></svg>
  <div class="abs foot-text" style="left:190px;top:4004px">Lichtbogenweg 7,<br>82041 Oberhaching<br>Germany</div>
  <svg class="abs" style="left:160px;top:4070px" width="14" height="10" viewBox="0 0 14 10"><rect x=".7" y=".7" width="12.6" height="8.6" stroke="#45e9f0" fill="none"/><path d="M1 1L7 6L13 1" stroke="#45e9f0" fill="none"/></svg>
  <div class="abs foot-text" style="left:190px;top:4066px">info@lumorix7.de</div>
  <svg class="abs" style="left:160px;top:4096px" width="13" height="13" viewBox="0 0 13 13"><path d="M2 1L5 1L6 4L4.5 5.2A7 7 0 0 0 7.8 8.5L9 7L12 8V11C12 11.6 11.5 12 11 12C5.5 12 1 7.5 1 2C1 1.5 1.4 1 2 1Z" stroke="#45e9f0" fill="none"/></svg>
  <div class="abs foot-text" style="left:190px;top:4094px">+00 1234 5678 9</div>
  <span class="abs" style="left:189px;top:4140px;width:16px;height:16px;border-radius:50%;background:#fff"></span>
  <span class="abs" style="left:224px;top:4140px;width:16px;height:16px;border-radius:50%;background:#fff"></span>
  <span class="abs" style="left:257px;top:4140px;width:16px;height:16px;border-radius:50%;background:#fff"></span>

  <div class="abs foot-head" style="left:477px;top:4007px">PARTNER LINKS</div>
  <ul class="abs foot-list" style="left:477px;top:4030px"><li>Jorin Valtke Kreativstudio</li><li>Grünbote</li><li>Kanal Neun Medienservice</li></ul>
  <div class="abs foot-head" style="left:748px;top:4007px">QUICK LINKS</div>
  <ul class="abs foot-list" style="left:748px;top:4030px"><li>Über uns</li><li>Sevices</li><li>Kontakt</li></ul>
  <ul class="abs foot-list" style="left:890px;top:4030px"><li>Cookie-Richtlinie (EU)</li><li>Haftungsausschluss</li><li>Impressum</li></ul>

  <div class="abs to-top"><svg width="32" height="32" viewBox="0 0 32 32"><path d="M11 18L16 13L21 18" stroke="#0d2150" stroke-width="1.6" fill="none"/></svg></div>
  <div class="abs copyright">© Copyright 2023 by LUMORIX 7, All Rights Reserved.</div>
</footer>

</body>
</html>
```